business card for a massage therapy practice named 'Meadow and Willow Massage Studio'

I really need a trendy, yet easy on the eyes business card to complement my logo. Ideally with some gold or rose gold foil work.

My uploaded file of the logo I have in horizontal but I have a vertical version as well. Another color that is used in the website is a blush pink here and there. I'd like to see some trendy tropical leaves in the design.

```html
<!DOCTYPE html>
<html lang="en">
<head>
<meta charset="utf-8">
<title>Meadow &amp; Willow Massage Studio – Business Card</title>
<link href="https://fonts.googleapis.com/css2?family=Oswald:wght@500&family=Lato:wght@400&display=swap" rel="stylesheet">
<style>
  :root {
    --backdrop: #5b5b5b;
    --paper: #fdfdfc;
    --ink: #1c1c1c;
    --teal: #7fd3bd;
    --gold: #9b8460;
    --charcoal: #3a3a3a;
    --muted: #555;
  }
  * { margin: 0; padding: 0; box-sizing: border-box; }
  html, body { width: 1200px; height: 1200px; overflow: hidden; }
  body { background: var(--backdrop); position: relative; font-family: "Lato", sans-serif; }

  .card {
    position: absolute;
    left: 174px;
    width: 852px;
    height: 486px;
    background: var(--paper);
    overflow: hidden;
  }
  .card--front { top: 52px; }
  .card--back { top: 661px; }

  .brand { position: absolute; display: flex; align-items: center; }
  .brand__mark { border-radius: 50%; background: var(--gold); flex: none; }
  .brand__name {
    font-family: "Oswald", sans-serif;
    font-weight: 500;
    color: var(--ink);
    line-height: 1.05;
    letter-spacing: 0.04em;
  }
  .brand__name span { display: block; }

  .card--front .brand { left: 56px; top: 148px; gap: 34px; }
  .card--front .brand__mark { width: 120px; height: 120px; }
  .card--front .brand__name { font-size: 66px; }
  .card--front .brand__name .brand__sub { font-size: 40px; letter-spacing: 0.2em; margin-top: 10px; }

  .card--back .brand { left: 150px; top: 36px; gap: 26px; }
  .card--back .brand__mark { width: 92px; height: 92px; }
  .card--back .brand__name { font-size: 52px; }
  .card--back .brand__name .brand__sub { font-size: 32px; letter-spacing: 0.2em; margin-top: 8px; }

  .person { position: absolute; left: 48px; top: 254px; }
  .person__name {
    font-family: "Oswald", sans-serif;
    font-weight: 500;
    font-size: 36px;
    letter-spacing: 0.03em;
    color: var(--ink);
    line-height: 1;
  }
  .person__role { font-size: 17px; color: var(--gold); margin-top: 2px; }

  .divider {
    position: absolute;
    left: 48px; top: 348px;
    width: 724px; height: 3px;
    background: var(--teal);
  }

  .contact { position: absolute; left: 48px; top: 362px; list-style: none; }
  .contact li {
    display: flex; align-items: center;
    height: 26px;
    font-size: 18px;
    color: var(--ink);
  }
  .contact svg { width: 18px; height: 18px; margin-right: 19px; stroke: var(--muted); fill: none; stroke-width: 1.4; }

  .address {
    position: absolute; left: 488px; top: 370px;
    font-size: 18px; line-height: 23px; color: var(--ink);
  }

  .footer-band { position: absolute; left: 0; bottom: 0; width: 100%; height: 32px; display: flex; }
  .footer-band__gold { width: 488px; background: var(--gold); }
  .footer-band__dark { flex: 1; background: var(--charcoal); }
</style>
</head>
<body>

<section class="card card--front">
  <div class="brand">
    <div class="brand__mark"></div>
    <div class="brand__name">
      <span>MEADOW &amp; WILLOW</span>
      <span class="brand__sub">MASSAGE STUDIO</span>
    </div>
  </div>
</section>

<section class="card card--back">
  <div class="brand">
    <div class="brand__mark"></div>
    <div class="brand__name">
      <span>MEADOW &amp; WILLOW</span>
      <span class="brand__sub">MASSAGE STUDIO</span>
    </div>
  </div>

  <div class="person">
    <div class="person__name">CLARA BENSON</div>
    <div class="person__role">manager</div>
  </div>

  <div class="divider"></div>

  <ul class="contact">
    <li>
      <svg viewBox="0 0 20 20"><path d="M4 3l3 0 1.5 4-2 1.2a9 9 0 0 0 5.3 5.3L13 11.5l4 1.5v3a2 2 0 0 1-2 2A13 13 0 0 1 2 5a2 2 0 0 1 2-2z"/></svg>
      +555-555-0148
    </li>
    <li>
      <svg viewBox="0 0 20 20"><rect x="2" y="4.5" width="16" height="11"/><path d="M2 4.5l8 6 8-6"/></svg>
      hello@meadowwillow.com
    </li>
    <li>
      <svg viewBox="0 0 20 20"><circle cx="10" cy="10" r="8"/><ellipse cx="10" cy="10" rx="3.5" ry="8"/><path d="M2 10h16M3.5 6h13M3.5 14h13"/></svg>
      www.meadowwillow.com
    </li>
  </ul>

  <address class="address" style="font-style: normal;">
    42 Orchard Lane 8<br>
    CANADA - B214
  </address>

  <div class="footer-band">
    <div class="footer-band__gold"></div>
    <div class="footer-band__dark"></div>
  </div>
</section>

</body>
</html>
```